Business Card Design for Venture Kite

Venture Kite is a pro bono student consultancy service offered by Corvala KTRB to social start ups and enterprises. We provide consulting services with expertise in areas such as Marketing, IT, Business Strategy and Innovation.
I have attached\ the Venture Kite Logo here for your perusal.
Industry/Entity Type
Business
Contact Information for Business Card
Name: Ha Min Park Name: Thomas Leung
Role: Project Leader Role: Vice Project Leader
M:0477203941 M: 0479352806
E: ha-min.park@corvalaktrb.org E: thomas.leung@corvalaktrb.org
W: www.corvalaktrb.org W: www.corvalaktrb.org

```html
<!DOCTYPE html>
<html lang="en">
<head>
<meta charset="utf-8">
<title>Venture Kite – Business Card</title>
<link href="https://fonts.googleapis.com/css2?family=Oswald:wght@300;400;700&display=swap" rel="stylesheet">
<style>
  :root {
    --bg: #e6e4e0;
    --card: #ffffff;
    --ink: #1c1c1c;
    --text: #333333;
    --gold: #e8b64a;
    --rule: #d4d4d4;
  }
  * { box-sizing: border-box; margin: 0; padding: 0; }
  html, body { width: 1200px; height: 886px; overflow: hidden; }
  body {
    background: var(--bg);
    font-family: "Oswald", sans-serif;
    display: flex;
    align-items: center;
    justify-content: center;
    gap: 40px;
  }
  .card {
    width: 540px;
    height: 330px;
    background: var(--card);
    border-radius: 16px;
    box-shadow: 0 2px 10px rgba(0,0,0,0.12);
    position: relative;
  }
  /* front */
  .card-front .brand {
    position: absolute;
    top: 40px;
    left: 0;
    width: 100%;
    text-align: center;
    font-weight: 700;
    font-size: 50px;
    letter-spacing: 1px;
    color: var(--ink);
    text-transform: uppercase;
    line-height: 1;
  }
  .contacts {
    position: absolute;
    top: 140px;
    left: 34px;
    right: 28px;
    bottom: 34px;
    display: flex;
  }
  .contact { flex: 1; padding-right: 16px; }
  .contact + .contact { padding-left: 22px; border-left: 1px solid var(--rule); }
  .contact-name {
    font-weight: 400;
    font-size: 22px;
    color: var(--text);
    text-transform: uppercase;
    line-height: 1.1;
  }
  .contact-role {
    font-weight: 300;
    font-size: 13px;
    color: var(--gold);
    text-transform: uppercase;
    letter-spacing: 0.4px;
    margin-bottom: 14px;
  }
  .detail {
    display: flex;
    align-items: center;
    gap: 9px;
    font-weight: 300;
    font-size: 13px;
    color: var(--text);
    margin-bottom: 7px;
    white-space: nowrap;
  }
  .icon {
    width: 16px;
    height: 16px;
    flex: none;
    background: var(--ink);
    display: flex;
    align-items: center;
    justify-content: center;
  }
  .icon svg { width: 12px; height: 12px; }
  /* back */
  .card-back .brand {
    position: absolute;
    top: 112px;
    left: 0;
    width: 100%;
    text-align: center;
    font-weight: 700;
    font-size: 58px;
    letter-spacing: 1px;
    color: var(--ink);
    text-transform: uppercase;
    line-height: 1;
  }
  .card-back .site {
    position: absolute;
    bottom: 40px;
    width: 100%;
    text-align: center;
    font-weight: 400;
    font-size: 18px;
    color: var(--gold);
    letter-spacing: 0.5px;
  }
</style>
</head>
<body>

<section class="card card-front">
  <h1 class="brand">Venture Kite</h1>
  <div class="contacts">
    <div class="contact">
      <p class="contact-name">Thomas Leung</p>
      <p class="contact-role">Vice Project Leader</p>
      <p class="detail"><span class="icon"><svg viewBox="0 0 12 12"><path d="M2 1.5 L4 1 L5 3.5 L4 4.5 Q5 7 7.5 8 L8.5 7 L11 8 L10.5 10 Q5 10.5 1.5 2.5 Z" fill="#e8b64a"/></svg></span>0479352806</p>
      <p class="detail"><span class="icon"><svg viewBox="0 0 12 12"><rect x="1" y="2.5" width="10" height="7" fill="#e8b64a"/><path d="M1 2.5 L6 6.5 L11 2.5" stroke="#1c1c1c" stroke-width="1" fill="none"/></svg></span>thomas.leung@corvalaktrb.org</p>
      <p class="detail"><span class="icon"><svg viewBox="0 0 12 12"><circle cx="6" cy="6" r="4.6" fill="#e8b64a"/><ellipse cx="6" cy="6" rx="2" ry="4.6" fill="none" stroke="#1c1c1c" stroke-width="0.8"/><line x1="1.4" y1="6" x2="10.6" y2="6" stroke="#1c1c1c" stroke-width="0.8"/></svg></span>www.corvalaktrb.org</p>
    </div>
    <div class="contact">
      <p class="contact-name">Ha Min Park</p>
      <p class="contact-role">Project Leader</p>
      <p class="detail"><span class="icon"><svg viewBox="0 0 12 12"><path d="M2 1.5 L4 1 L5 3.5 L4 4.5 Q5 7 7.5 8 L8.5 7 L11 8 L10.5 10 Q5 10.5 1.5 2.5 Z" fill="#e8b64a"/></svg></span>0477203941</p>
      <p class="detail"><span class="icon"><svg viewBox="0 0 12 12"><rect x="1" y="2.5" width="10" height="7" fill="#e8b64a"/><path d="M1 2.5 L6 6.5 L11 2.5" stroke="#1c1c1c" stroke-width="1" fill="none"/></svg></span>ha-min.park@corvalaktrb.org</p>
      <p class="detail"><span class="icon"><svg viewBox="0 0 12 12"><circle cx="6" cy="6" r="4.6" fill="#e8b64a"/><ellipse cx="6" cy="6" rx="2" ry="4.6" fill="none" stroke="#1c1c1c" stroke-width="0.8"/><line x1="1.4" y1="6" x2="10.6" y2="6" stroke="#1c1c1c" stroke-width="0.8"/></svg></span>www.corvalaktrb.org</p>
    </div>
  </div>
</section>

<section class="card card-back">
  <h2 class="brand">Venture Kite</h2>
  <p class="site">www.corvalaktrb.org</p>
</section>

</body>
</html>
```